Famous Australian Web Brand (Zentrivo.com.au) Needs a New Website & Logo

Zentrivo.com.au is one of the leading domain name registration businesses in Australia and is looking for an overhaul of its website and brand.

Zentrivo.com.au current products/services include domain name registration, web hosting, web site creation and SSL certificates.

In this design contest on Quorvane, we would like designers to create a new logo and new website design for Zentrivo.com.au.

Here is what contest entrants will need to create:
- 1 new logo
- 1 new home page design
- 1 internal page (pricing page)

The winning designer will receive the main prize of $750. In addition to this, the winning designer will have the opportunity to work with Zentrivo for the build of the full website and may get ongoing design work from Zentrivo.

thank you all for your designs, we are after a web 2.0 look and feel, please dont use serif fonts, lets use modern and sleek ones, i will upload some samples of one we like shortly

header is to be in black with some texturing, white fonts and the call to action buttons are in green.

for the 6 free services, please use round edges for the images with the text under it, as i will upload shortly and we would like custome images, not stockimage types please

im uploading a sample of a background image for the header, which is black with texturing and also and image for the footer/middle of the page which has the correct shading of the grey for the middle section

please see file 8 for the look we are trying to get with our site and for font ideas

Reason: we have decided to extend the contest for another 3 days as a couple of designers have requested a bit more time

Target Market(s)

People that might need to buy a domain name or start a website: small business owners; entrepreneurs; bloggers; everyone from mum-and-dad website owners to tech savvy entrepreneurs. Geographically we will be targeting Australia but this should not influence the design.

Industry/Entity Type

Build

Requirements
Must have
• The logo should:
- Have the text "Zentrivo"
- Be positioned in the top left hand corner of the website
- Be either a wordmark, pictorial or abstract logo. That is, text-only logos are acceptable but we are also interested in receiving logos with a mark to the left that could somehow represents the business that we’re in

The homepage should:
- Feel modern, slick, web2.0
- Have a horizontal menu with 4 menu items: About Us | Contact Us | My Cart | Login
- Include the logo at the top
- Include the content from this Word Document
- Include the rough layout and style from this JPG template layout

The interior page should:
- Have the same look and feel as the home page
- Include the rough layout and style from this JPG attachment
- Include the content from this second Word Document
Nice to have
• - Grey, white and black primary colors
- Buttons that are green or lime green with a web2.0 call to action
- Full-width design (i.e. across the screen like Quorvane)
Should not have
• - Do not include overt Australian references. While we are an Australian business we do not want Australian flags, kangaroos or Barnaby Wollop in our logo or on our website.
- Do not use the current red color scheme in the design. We want to move away from this.

```html
<!DOCTYPE html>
<html lang="en">
<head>
<meta charset="utf-8">
<title>Zentrivo – Domain Names</title>
<link href="https://fonts.googleapis.com/css2?family=Arimo:ital,wght@0,400;0,700;1,700&family=Orbitron:wght@500&display=swap" rel="stylesheet">
<style>
:root{
  --green:#7cc424;
  --green-dark:#5e9e12;
  --green-text:#8fd12f;
  --ink:#1b1b1b;
  --header-top:#2c2c2c;
  --header-bottom:#121212;
  --nav:#0b0b0b;
  --grey-mid:#bdbdbd;
  --grey-light:#d9d9d9;
  --card:#e2e2e2;
  --panel:#0f0f0f;
  --white:#ffffff;
  --muted:#8a8a8a;
}
*{box-sizing:border-box;margin:0;padding:0}
html,body{width:1200px;height:800px;overflow:hidden}
body{font-family:"Arimo",Arial,sans-serif;background:var(--grey-mid);position:relative;color:var(--ink)}
.abs{position:absolute}

.site-header{left:0;top:0;width:1200px;height:150px;background:linear-gradient(var(--header-top),var(--header-bottom))}
.call-tab{left:430px;top:0;width:340px;height:36px;background:linear-gradient(#8fd63a,#5fa616);border-radius:0 0 5px 5px;color:var(--white);font-weight:700;font-size:14px;text-align:center;line-height:34px}
.top-menu{right:110px;top:10px;font-size:13px;color:var(--green-text);letter-spacing:.2px}
.brand{left:112px;top:58px;font-size:44px;font-weight:700;color:var(--green-text);letter-spacing:1px}
.tagline{left:118px;top:105px;font-size:16px;color:var(--white)}
.tagline b{color:var(--green-text)}
.search-field{left:620px;top:71px;width:281px;height:30px;background:#bdbdbd;border-radius:4px;font-size:14px;color:#4a4a4a;padding:7px 10px}
.tld-select{left:911px;top:71px;width:84px;height:30px;background:#3a3a3a;border-radius:4px;color:var(--white);font-size:14px;padding:7px 10px}
.tld-select span{position:absolute;right:0;top:0;width:26px;height:30px;background:#6a6a6a;border-radius:0 4px 4px 0}
.tld-select svg{position:absolute;right:7px;top:12px}
.search-btn{left:1006px;top:71px;width:84px;height:30px;background:linear-gradient(#8fd63a,#5fa616);border-radius:4px;color:var(--white);font-size:14px;text-align:center;line-height:30px}
.sub-links{right:112px;top:110px;font-size:9px;color:#6d6d6d;word-spacing:1px}
.sub-links span{margin-left:12px}

.main-nav{left:0;top:150px;width:1200px;height:40px;background:var(--nav);display:flex;padding-left:106px;gap:9px;align-items:center}
.main-nav a{color:var(--white);font-size:14.5px;text-decoration:none}
.main-nav a::before{content:"";display:inline-block;border-left:4px solid var(--green);border-top:4px solid transparent;border-bottom:4px solid transparent;margin-right:5px;vertical-align:1px}

.stage{left:0;top:190px;width:1200px;height:510px;background:radial-gradient(ellipse at 50% 30%,var(--grey-light),#b4b4b4 80%)}

.video-card{top:200px;width:320px;height:140px;background:linear-gradient(#ececec,#d4d4d4);border-radius:5px;overflow:hidden}
.video-card::after{content:"";position:absolute;left:0;bottom:0;width:100%;height:14px;background:linear-gradient(#8fd63a,#5fa616)}
.video-thumb{position:absolute;left:8px;top:8px;width:128px;height:107px;border:3px solid var(--green);background:linear-gradient(135deg,#c9b07c,#efe6d6 60%,#d7cbb8)}
.play{position:absolute;left:0;bottom:0;width:28px;height:28px;background:var(--green)}
.video-card h3{position:absolute;left:142px;top:8px;font-size:18px;font-weight:400;color:var(--green-text);line-height:19px}
.video-card p{position:absolute;left:142px;top:24px;font-size:12px;color:#2e2e2e}
.video-label{position:absolute;right:8px;bottom:17px;font-size:12px;font-style:italic;font-weight:700;color:#b5b5b5}

.promise{left:0;top:354px;width:1200px;text-align:center;font-style:italic;font-weight:700}
.promise .line1{font-size:15px;line-height:18px;color:#3a3a3a}
.promise .line2{font-size:22px;line-height:24px;color:var(--green-text)}
.promise .q{font-size:42px;line-height:0;color:#333;vertical-align:-12px;font-style:normal}

.feature{top:410px;width:460px;height:280px;background:var(--panel);border-radius:5px}
.feature-media{position:absolute;left:11px;top:10px;width:438px;height:165px;border:3px solid var(--green)}
.feature h4{position:absolute;left:13px;top:189px;font-size:14px;color:var(--green-text)}
.feature p{position:absolute;left:13px;top:205px;width:430px;font-size:12px;line-height:14.5px;color:var(--white)}

.arrow{top:520px}

.site-footer{left:0;top:700px;width:1200px;height:100px;background:#1c1c1c}
.legal{left:110px;top:727px;font-size:9px;color:var(--white);line-height:12px}
.footer-cta{right:112px;top:711px;text-align:right;font-family:"Orbitron",Arial,sans-serif;color:var(--white);font-size:15px;line-height:22px;letter-spacing:.5px}
.footer-cta em{font-style:normal;color:var(--green-text)}
</style>
</head>
<body>

<header class="site-header abs"></header>
<div class="call-tab abs">Have a question? Call now 1300 41 72 95</div>
<nav class="top-menu abs">ABOUT US | CONTACT US | MY CART | LOGIN</nav>
<div class="brand abs">Zentrivo</div>
<div class="tagline abs"><b>“</b>You get a lot more than just a domain name<b>”</b></div>
<div class="search-field abs">www.</div>
<div class="tld-select abs">.com<span></span><svg width="12" height="7"><path d="M0 0h12L6 7z" fill="#2a2a2a"/></svg></div>
<div class="search-btn abs">search</div>
<div class="sub-links abs"><span>RENEW A DOMAIN</span><span>TRANSFER A DOMAIN</span><span>VIEW PRICE LIST</span></div>

<nav class="main-nav abs">
  <a href="#">DOMAINS</a><a href="#">CREATOR</a><a href="#">EMAIL</a><a href="#">HOSTING</a><a href="#">MARKETING</a>
</nav>

<main>
  <div class="stage abs"></div>

  <article class="video-card abs" style="left:110px">
    <div class="video-thumb" role="img" aria-label="Video still of a presenter"><div class="play"><svg width="28" height="28"><path d="M10 8l10 6-10 6z" fill="#fff"/></svg></div></div>
    <h3>EVERYONE NEEDS</h3><p>A DOMAIN NAME</p><span class="video-label">VIDEOS</span>
  </article>
  <article class="video-card abs" style="left:440px">
    <div class="video-thumb" role="img" aria-label="Video still of a presenter"><div class="play"><svg width="28" height="28"><path d="M10 8l10 6-10 6z" fill="#fff"/></svg></div></div>
    <h3>HOW YOU CAN</h3><p>USE A DOMAIN NAME</p><span class="video-label">VIDEOS</span>
  </article>
  <article class="video-card abs" style="left:770px">
    <div class="video-thumb" role="img" aria-label="Video still of a presenter"><div class="play"><svg width="28" height="28"><path d="M10 8l10 6-10 6z" fill="#fff"/></svg></div></div>
    <h3>WHY CHOOSE</h3><p>DOMAIN NAMES</p><span class="video-label">VIDEOS</span>
  </article>

  <div class="promise abs">
    <div class="line1"><span class="q">“</span> Everything your business needs to be successful online is <span class="q">”</span></div>
    <div class="line2">FREE with every domain name.</div>
  </div>

  <svg class="arrow abs" style="left:100px" width="28" height="50" aria-hidden="true"><path d="M28 0A25 25 0 0 0 28 50z" fill="var(--green)"/><path d="M20 18v14l-9-7z" fill="#fff"/></svg>
  <svg class="arrow abs" style="left:1072px" width="28" height="50" aria-hidden="true"><path d="M0 0A25 25 0 0 1 0 50z" fill="var(--green)"/><path d="M8 18v14l9-7z" fill="#fff"/></svg>

  <section class="feature abs" style="left:135px">
    <div class="feature-media" role="img" aria-label="Collage of colourful website templates" style="background:linear-gradient(90deg,#3f8f3a,#d9d3c0 35%,#e8e1d2 60%,#3c6fb0 85%,#e0e0e0)"></div>
    <h4>FREE 15 PAGE WEBSITE</h4>
    <p>Create a professional, full-featured website in minutes without any technical knowledge. Choose from 4,000+ stunning website designs and customize your site with near-limitless options. Upload your own artwork for a truly personalised look.</p>
  </section>
  <section class="feature abs" style="left:604px">
    <div class="feature-media" role="img" aria-label="Screenshot of an email inbox application" style="background:linear-gradient(#dfe8f3,#f4f6f9 40%,#e7ebf0)"></div>
    <h4>FREE PROFESSIONAL EMAIL</h4>
    <p>Having a personalised address that matches your domain name<br>(for example, Ned@NedsMuffins.com or Sales@NedsMuffins.com) gives your company a much more professional image when you communicate with customers and associates.</p>
  </section>
</main>

<footer class="site-footer abs"></footer>
<div class="legal abs">COPYRIGHT © 2010 ZENTRIVO.<br>USE OF THIS WEBSITE CONSTITUTES ACCEPTANCE OF OUR USER AGREEMENT AND PRIVACY POLICY.</div>
<div class="footer-cta abs">HAVE A QUESTION FOR US?<br>CONTACT US <em>1300 41 72 95</em></div>

</body>
</html>
```